Gentleman's grooming products require a business card

I need a business card that incorporates the logo [ or parts of ] that we had Pixel Hive design for us as uploaded.

We sell online, mens grooming products including moustache waxes, beard oils and shaving accessories.
We want a card that is classy, professional and a card that shouts mens products.

Target Market(s)

Young professional male market

Industry/Entity Type

Business

Contact Information for Business Card

Ross and Edith Carwell
Lather and Lore
Suppliers of fine moustache waxes, beard oils and shaving goods
M :0418529647
E : ross@latherandlore.com.au
E : edith@latherandlore.com.au
E : sales@theblokesbalmery.com.au

W : www.latherandlore.com.au

Requirements
Must have
• Class
Nice to have
• Professionalism

```html
<!DOCTYPE html>
<html lang="en">
<head>
<meta charset="utf-8">
<title>Lather and Lore — Business Card</title>
<link href="https://fonts.googleapis.com/css2?family=Cinzel:wght@400;600&family=Roboto+Condensed:wght@400;700&display=swap" rel="stylesheet">
<style>
  :root {
    --bg: #8e8e8e;
    --bg-light: #bdbdbd;
    --gold-1: #f7a600;
    --gold-2: #ffd21c;
    --ink: #111111;
    --card-black: #0b0b0b;
    --paper: #ffffff;
  }
  * { box-sizing: border-box; margin: 0; padding: 0; }
  html, body { width: 1200px; height: 960px; overflow: hidden; }
  body {
    background: radial-gradient(ellipse at 55% 40%, var(--bg-light), var(--bg));
    position: relative;
  }
  .card {
    position: absolute;
    left: 220px;
    width: 760px;
    height: 434px;
    overflow: hidden;
    box-shadow: 0 10px 28px rgba(0,0,0,.35);
  }
  /* Front */
  .card--front {
    top: 30px;
    background: linear-gradient(100deg, var(--gold-1), var(--gold-2));
    color: var(--ink);
  }
  .front__rule {
    position: absolute; left: 70px; right: 70px; height: 2px; background: var(--ink);
  }
  .front__rule--top { top: 110px; }
  .front__rule--bottom { top: 290px; }
  .front__mark {
    position: absolute; left: 350px; top: 70px; width: 60px; height: 60px;
    border: 2px solid var(--ink); background: var(--gold-2);
  }
  .front__name {
    position: absolute; left: 0; right: 0; top: 160px; text-align: center;
    font-family: "Cinzel", serif; font-weight: 600; font-size: 70px; letter-spacing: 1px;
  }
  .front__tagline {
    position: absolute; left: 0; right: 0; top: 306px; text-align: center;
    font-family: "Cinzel", serif; font-size: 19px; letter-spacing: .5px;
  }
  /* Back */
  .card--back {
    top: 496px;
    background: var(--card-black);
    color: var(--paper);
  }
  .back__mark {
    position: absolute; left: 100px; top: 60px; width: 56px; height: 56px;
    border: 2px solid var(--paper);
  }
  .back__brand {
    position: absolute; left: 50px; top: 140px; width: 320px; text-align: center;
    font-family: "Cinzel", serif; font-weight: 600; font-size: 34px; line-height: 1.15;
  }
  .back__rule {
    position: absolute; left: 0; right: 0; top: 330px; height: 2px; background: var(--paper);
  }
  .back__tagline {
    position: absolute; left: 0; right: 0; top: 346px; text-align: center;
    font-family: "Cinzel", serif; font-size: 19px; letter-spacing: .5px;
  }
  .contact {
    position: absolute; right: 30px; top: 44px; width: 380px; text-align: right;
    font-family: "Roboto Condensed", sans-serif;
  }
  .contact__names { font-weight: 700; font-size: 28px; margin-bottom: 22px; margin-right: 4px; }
  .contact__row {
    display: flex; justify-content: flex-end; align-items: center;
    font-size: 19px; height: 36px;
  }
  .contact__line { width: 22px; height: 2px; background: var(--paper); margin: 0 4px 0 8px; }
  .contact__icon {
    width: 26px; height: 26px; border-radius: 50%; background: var(--paper);
    display: flex; align-items: center; justify-content: center;
  }
  .contact__web { font-weight: 700; font-size: 21px; margin-top: 18px; margin-right: 4px; }
</style>
</head>
<body>

<section class="card card--front" aria-label="Card front">
  <div class="front__rule front__rule--top"></div>
  <div class="front__mark"></div>
  <div class="front__name">Lather and Lore</div>
  <div class="front__rule front__rule--bottom"></div>
  <div class="front__tagline">SUPPLIERS OF FINE MOUSTACHE WAXES, BEARD OILS AND SHAVING GOODS</div>
</section>

<section class="card card--back" aria-label="Card back">
  <div class="back__mark"></div>
  <div class="back__brand">Lather and Lore</div>

  <div class="contact">
    <div class="contact__names">Ross and Edith Carwell</div>
    <div class="contact__row">0418529647<span class="contact__line"></span>
      <span class="contact__icon"><svg width="12" height="16" viewBox="0 0 12 16"><rect x="1.5" y="1" width="9" height="14" rx="1.5" fill="none" stroke="#0b0b0b" stroke-width="1.6"/><circle cx="6" cy="12.5" r="1" fill="#0b0b0b"/></svg></span></div>
    <div class="contact__row">ross@latherandlore.com.au<span class="contact__line"></span>
      <span class="contact__icon"><svg width="16" height="12" viewBox="0 0 16 12"><rect x="1" y="1" width="14" height="10" fill="#0b0b0b"/><path d="M1 1l7 6 7-6" fill="none" stroke="#fff" stroke-width="1.2"/></svg></span></div>
    <div class="contact__row">edith@latherandlore.com.au<span class="contact__line"></span>
      <span class="contact__icon"><svg width="16" height="12" viewBox="0 0 16 12"><rect x="1" y="1" width="14" height="10" fill="#0b0b0b"/><path d="M1 1l7 6 7-6" fill="none" stroke="#fff" stroke-width="1.2"/></svg></span></div>
    <div class="contact__row">sales@theblokesbalmery.com.au<span class="contact__line"></span>
      <span class="contact__icon"><svg width="16" height="12" viewBox="0 0 16 12"><rect x="1" y="1" width="14" height="10" fill="#0b0b0b"/><path d="M1 1l7 6 7-6" fill="none" stroke="#fff" stroke-width="1.2"/></svg></span></div>
    <div class="contact__web">www.latherandlore.com.au</div>
  </div>

  <div class="back__rule"></div>
  <div class="back__tagline">SUPPLIERS OF FINE MOUSTACHE WAXES, BEARD OILS AND SHAVING GOODS</div>
</section>

</body>
</html>
```